Mobile Fitness snd Therapy Business Card Design

I need a business card designed for my mobile fitness and therapy business.

Please view the images that I have uploaded. I like the simplicity of the design that I have attached. I adapted it with my information

Target Market(s)

Those seeking personal training, injury rehabilitation or massage therapy.

Industry/Entity Type

Business

Contact Information for Business Card

Derek Holloway - MSc, CAT(C), RMT, CSCS, Pn2
e-mail: derek@bravuumfit.example
website: www.bravuumfit.example
instagram: @derek_holloway

Font styles to use
Sans Serif

Colors
3176b5
0355a3

Requirements
Must have
• "Contact us to receive a FREE assessment"
• Services offered:
• Personal Training
• Golf Fitness
• Injury Rehab
• Massage Therapy
• Yoga
Nice to have
• Consistent colours with brand
• - Dark Blue: #232837
• - Blue: #5096f0
• Consistent look/feel with the website: www.bravuumfit.example

```html
<!DOCTYPE html>
<html lang="en">
<head>
<meta charset="utf-8">
<title>Bravuum Business Card</title>
<link rel="stylesheet" href="https://fonts.googleapis.com/css2?family=Montserrat:wght@600&family=Archivo:wght@800&family=Noto+Serif:wght@400;700&family=Nunito+Sans:wght@400;600&display=swap">
<style>
  :root {
    --navy: #232837;
    --blue: #3176b5;
    --blue-deep: #0355a3;
    --blue-bright: #5096f0;
    --white: #ffffff;
    --stage: #e8edf4;
    --muted: #3a3f4c;
  }
  * { box-sizing: border-box; margin: 0; padding: 0; }
  html, body { width: 1200px; height: 1000px; overflow: hidden; }
  body {
    background: var(--stage);
    display: flex;
    align-items: center;
    justify-content: center;
    gap: 60px;
  }
  .card {
    width: 520px;
    height: 297px;
    position: relative;
    overflow: hidden;
    box-shadow: 0 8px 24px rgba(35, 40, 55, 0.18);
  }
  .card--front { background: var(--white); }
  .card--back { background: var(--navy); }

  .brand {
    height: 84px;
    display: flex;
    align-items: center;
    justify-content: center;
    gap: 12px;
    font-family: "Montserrat", sans-serif;
    font-weight: 600;
    font-size: 36px;
    letter-spacing: 5px;
  }
  .brand__mark { width: 14px; height: 14px; background: var(--blue-bright); }
  .card--front .brand { color: var(--navy); }
  .card--back .brand { color: var(--white); }

  .offer-band {
    height: 42px;
    display: flex;
    align-items: center;
    justify-content: center;
    font-family: "Noto Serif", serif;
    font-size: 19px;
  }
  .card--front .offer-band { background: var(--navy); color: var(--white); }
  .card--back .offer-band { background: var(--white); color: var(--navy); }
  .offer-band__free {
    font-weight: 700;
    font-size: 22px;
    color: var(--blue-bright);
    margin: 0 6px;
  }
  .card--back .offer-band__free { color: var(--blue); }

  .identity { text-align: center; padding-top: 34px; }
  .identity__name {
    font-family: "Archivo", sans-serif;
    font-weight: 800;
    font-size: 30px;
    color: var(--blue);
    letter-spacing: 0.5px;
  }
  .identity__credentials {
    font-family: "Noto Serif", serif;
    font-size: 12px;
    color: var(--blue);
    margin-top: 2px;
  }

  .contact-row {
    position: absolute;
    left: 0; right: 0; bottom: 16px;
    display: flex;
    justify-content: center;
    gap: 18px;
    font-family: "Nunito Sans", sans-serif;
    font-size: 11px;
    color: var(--muted);
  }
  .contact-row__item { display: flex; align-items: center; gap: 5px; }
  .contact-row__item svg { width: 13px; height: 13px; }

  .services { text-align: center; padding-top: 30px; font-family: "Nunito Sans", sans-serif; }
  .services__title {
    font-weight: 400;
    font-size: 22px;
    color: var(--blue-bright);
    letter-spacing: 1px;
    margin-bottom: 8px;
  }
  .services__line { font-size: 16px; color: #dfe3ea; line-height: 1.45; }
  .services__dot { margin: 0 6px; }
</style>
</head>
<body>

  <section class="card card--front" aria-label="Business card front">
    <div class="brand"><span class="brand__mark"></span>BRAVUUM</div>
    <div class="offer-band">Contact us to receive a<span class="offer-band__free">FREE</span>assessment</div>
    <div class="identity">
      <h1 class="identity__name">DEREK HOLLOWAY</h1>
      <p class="identity__credentials">MSc, CAT(C), RMT, CSCS, Pn2</p>
    </div>
    <div class="contact-row">
      <span class="contact-row__item">
        <svg viewBox="0 0 16 16" fill="none" stroke="currentColor" stroke-width="1.3"><rect x="1.5" y="3.5" width="13" height="9"/><path d="M1.5 3.5 8 9l6.5-5.5"/></svg>
        derek@bravuumfit.example
      </span>
      <span class="contact-row__item">
        <svg viewBox="0 0 16 16" fill="none" stroke="currentColor" stroke-width="1.3"><circle cx="8" cy="8" r="6.5"/><ellipse cx="8" cy="8" rx="3" ry="6.5"/><path d="M1.5 8h13"/></svg>
        www.bravuumfit.example
      </span>
      <span class="contact-row__item">
        <svg viewBox="0 0 16 16" fill="none" stroke="currentColor" stroke-width="1.3"><circle cx="8" cy="8" r="6.5"/></svg>
        @derek_holloway
      </span>
    </div>
  </section>

  <section class="card card--back" aria-label="Business card back">
    <div class="brand"><span class="brand__mark"></span>BRAVUUM</div>
    <div class="offer-band">Contact us to receive a<span class="offer-band__free">FREE</span>assessment</div>
    <div class="services">
      <h2 class="services__title">SERVICES OFFERED:</h2>
      <p class="services__line">Personal Training<span class="services__dot">•</span>Golf Fitness<span class="services__dot">•</span>Injury Rehab</p>
      <p class="services__line">Massage Therapy<span class="services__dot">•</span>Yoga</p>
    </div>
  </section>

</body>
</html>
```